San Francisco Pet Care Non Profit

Business Card Design for non profit organization.
We are a mobile pet care team who supports and attends to pets whose owners are homeless. Thanks for your help and creativity.

Industry/Entity Type

Non Profit

Contact Information for Business Card

Marisol Keddy
President
2871 Larkmoor Street, #512
San Francisco, CA 94187
phone: 415-729-3846
fax: 415-781-4052
marisol@tidywagonvan.org
website: tidywagonvan.org
facebook: facebook.com/TidyWagonVan

Font styles to use
Serif
Sans Serif

Colors

Designer to choose colors to be used in the design.

Requirements
Must have
• above details and attached logo

```html
<!DOCTYPE html>
<html lang="en">
<head>
<meta charset="utf-8">
<title>Tidy Wagon Van – Business Card</title>
<link href="https://fonts.googleapis.com/css2?family=Roboto:wght@300;400;700;900&display=swap" rel="stylesheet">
<style>
  :root {
    --brand-blue: #0aaeea;
    --ink: #1a1a1a;
    --muted: #555555;
    --paper: #ffffff;
    --backdrop: #2b2b2b;
  }
  * { box-sizing: border-box; margin: 0; padding: 0; }
  html, body { width: 1200px; height: 960px; overflow: hidden; }
  body {
    background: var(--backdrop);
    font-family: "Roboto", Arial, sans-serif;
    position: relative;
  }
  .card {
    position: absolute;
    width: 560px;
    height: 320px;
    overflow: hidden;
    box-shadow: 0 14px 30px rgba(0,0,0,.45);
  }
  /* Front side */
  .card-front {
    left: 60px; top: 110px;
    background: var(--brand-blue);
    color: var(--paper);
  }
  .front-mark {
    position: absolute;
    left: 0; right: 0; top: 96px;
    display: flex; align-items: center; justify-content: center; gap: 14px;
  }
  .front-mark .dot {
    width: 30px; height: 30px; border-radius: 50%;
    border: 3px solid var(--paper);
  }
  .front-mark .brand-name {
    font-size: 40px; font-weight: 700; color: var(--paper);
  }
  .front-url {
    position: absolute; left: 0; right: 0; bottom: 42px;
    text-align: center;
    font-size: 14px; font-weight: 300; letter-spacing: 7px;
  }
  /* Back side */
  .card-back {
    left: 580px; top: 500px;
    background: var(--paper);
  }
  .back-brand {
    position: absolute; right: 40px; top: 52px;
    display: flex; align-items: center; gap: 10px;
  }
  .back-brand .dot {
    width: 26px; height: 26px; border-radius: 50%;
    background: var(--brand-blue);
  }
  .back-brand .brand-name {
    font-size: 34px; font-weight: 700; color: var(--brand-blue); line-height: 1;
  }
  .back-brand .tagline {
    display: block; text-align: right;
    font-size: 12px; font-weight: 700; color: var(--ink); margin-top: 3px;
  }
  .person {
    position: absolute; left: 36px; top: 148px;
  }
  .person .name { font-size: 22px; font-weight: 700; color: var(--brand-blue); line-height: 1.05; }
  .person .role { font-size: 13px; font-weight: 700; color: var(--ink); margin-bottom: 8px; }
  .contacts { list-style: none; }
  .contacts li {
    display: flex; align-items: center; gap: 9px;
    font-size: 12.5px; color: var(--muted); line-height: 17px;
  }
  .contacts svg { width: 12px; height: 12px; fill: var(--brand-blue); flex: none; }
  .address-band {
    position: absolute; left: 0; right: 0; bottom: 0; height: 34px;
    background: var(--brand-blue); color: var(--paper);
    display: flex; align-items: center; justify-content: center;
    font-size: 14px; font-weight: 400; letter-spacing: .3px;
  }
</style>
</head>
<body>
  <section class="card card-front">
    <div class="front-mark">
      <span class="dot"></span>
      <span class="brand-name">TidyWagonVan</span>
    </div>
    <p class="front-url">www.tidywagonvan.org</p>
  </section>

  <section class="card card-back">
    <div class="back-brand">
      <span class="dot"></span>
      <div>
        <span class="brand-name">TidyWagonVan</span>
        <span class="tagline">Mobile Pet Care Team</span>
      </div>
    </div>

    <div class="person">
      <p class="name">Marisol Keddy</p>
      <p class="role">President</p>
      <ul class="contacts">
        <li><svg viewBox="0 0 12 12"><path d="M2.5 0.5 L4.5 0.5 L5 3 L3.6 4 Q4.6 6.6 7.8 8.2 L8.8 6.9 L11.5 7.4 L11.5 9.5 Q11 11.5 9 11.5 Q1 10 0.5 2.5 Q0.6 0.6 2.5 0.5Z"/></svg>415-729-3846</li>
        <li><svg viewBox="0 0 12 12"><path d="M3 0h6a1 1 0 0 1 1 1v10a1 1 0 0 1-1 1H3a1 1 0 0 1-1-1V1a1 1 0 0 1 1-1zm0.5 1.5v8h5v-8z"/></svg>415-781-4052</li>
        <li><svg viewBox="0 0 12 12"><path d="M0 2h12v8H0z M0.8 2.6 6 6.6 11.2 2.6" fill="var(--brand-blue)" stroke="#fff" stroke-width="0.9"/></svg>marisol@tidywagonvan.org</li>
        <li><svg viewBox="0 0 12 12"><circle cx="6" cy="6" r="5.5"/><path d="M0.5 6h11M6 0.5v11M6 0.5q-3 5.5 0 11M6 0.5q3 5.5 0 11" stroke="#fff" stroke-width="0.8" fill="none"/></svg>www.tidywagonvan.org</li>
        <li><svg viewBox="0 0 12 12"><rect width="12" height="12" rx="1.5"/></svg>/TidyWagonVan</li>
      </ul>
    </div>

    <div class="address-band">2871 Larkmoor Street, #512, San Francisco, CA 94187</div>
  </section>
</body>
</html>
```